Newsletter Banner Ad with a URL to our website offering

We need a banner ad for a newsletter that is published to members biweekly that simply articulates our value proposition and enables the reader to click on our logo to learn more and engage with us to schedule an Emergency Response Plan so they are ready for when a burst pipe happens on their property. They will have a plan after they engage with us.
We need quotes to build two options 1&2

```html
<!DOCTYPE html>
<html lang="en">
<head>
<meta charset="UTF-8">
<title>Crestway Restoration – Newsletter Banners</title>
<link rel="stylesheet" href="https://fonts.googleapis.com/css2?family=Arimo:wght@700&display=swap">
<style>
  :root {
    --page-bg: #fdfdfd;
    --brand-red: #c80000;
    --brand-navy: #00008f;
    --accent-red: #e8232b;
    --ink: #111111;
    --white: #ffffff;
    --mark-blue: #1c2fb0;
  }
  html, body {
    margin: 0;
    padding: 0;
    width: 1200px;
    height: 1000px;
    overflow: hidden;
    background: var(--page-bg);
    font-family: "Arimo", Arial, sans-serif;
  }
  .canvas {
    position: relative;
    width: 1200px;
    height: 1000px;
  }
  .banner {
    position: absolute;
    left: 170px;
    width: 861px;
    height: 222px;
    overflow: hidden;
    background: var(--white);
    box-shadow: 0 4px 9px rgba(0, 0, 0, 0.22);
  }
  .banner--option-one { top: 235px; }
  .banner--option-two { top: 569px; }

  .photo {
    position: absolute;
    top: 0;
    height: 100%;
  }
  .photo--flooded-hallway {
    left: 150px;
    width: 330px;
    background: linear-gradient(180deg,
      #d9d9de 0%, #eeeef2 12%, #cfcfd4 30%,
      #bdb7b4 52%, #a8826c 66%, #8c5a3e 82%, #6e3f28 100%);
    -webkit-mask-image: linear-gradient(90deg, transparent 0%, rgba(0,0,0,0.55) 25%, #000 50%);
    mask-image: linear-gradient(90deg, transparent 0%, rgba(0,0,0,0.55) 25%, #000 50%);
  }
  .photo--burst-pipe {
    left: 0;
    width: 440px;
    background:
      linear-gradient(180deg, rgba(255,255,255,0) 55%, rgba(255,255,255,0.5) 100%),
      linear-gradient(100deg, #a89d92 0%, #cfc8bf 25%, #e7e4df 50%, #f3f3f3 75%, #ececec 100%);
  }

  .panel-shape {
    position: absolute;
    top: 0;
    left: 0;
    width: 861px;
    height: 222px;
  }

  .brand-mark {
    position: absolute;
    display: flex;
    flex-direction: column;
    align-items: center;
    color: var(--ink);
    font-weight: 700;
    text-decoration: none;
    white-space: nowrap;
  }
  .brand-mark__circle {
    width: 60px;
    height: 60px;
    border-radius: 50%;
    background: var(--mark-blue);
    margin-bottom: 9px;
  }
  .brand-mark__name {
    font-size: 22px;
    line-height: 22px;
    letter-spacing: 2px;
  }
  .brand-mark__tagline {
    margin-top: 4px;
    font-size: 9.5px;
    line-height: 10px;
    letter-spacing: 2.4px;
  }
  .banner--option-one .brand-mark { left: 34px; top: 29px; width: 126px; }
  .banner--option-two .brand-mark { left: 226px; top: 22px; width: 126px; }

  .headline {
    position: absolute;
    margin: 0;
    color: var(--white);
    font-weight: 700;
  }
  .headline__lead {
    display: block;
    font-size: 53px;
    line-height: 52px;
    letter-spacing: -0.5px;
  }
  .headline__rest {
    display: block;
    font-size: 34px;
    line-height: 45px;
    margin-left: 3px;
  }
  .banner--option-one .headline { left: 476px; top: 54px; }
  .banner--option-two .headline { left: 443px; top: 52px; }
</style>
</head>
<body>
<div class="canvas">

  <section class="banner banner--option-one" aria-label="Banner option 1">
    <div class="photo photo--flooded-hallway" role="img" aria-label="Photo of a flooded office hallway with water on the floor"></div>
    <svg class="panel-shape" viewBox="0 0 861 222" aria-hidden="true">
      <path d="M463 0 Q 368 111 462 222 L861 222 L861 0 Z" fill="var(--brand-navy)"/>
      <path d="M472 0 Q 394 111 470 222 L861 222 L861 0 Z" fill="var(--brand-red)"/>
    </svg>
    <a class="brand-mark" href="#">
      <span class="brand-mark__circle"></span>
      <span class="brand-mark__name">CRESTWAY</span>
      <span class="brand-mark__tagline">RESTORATION</span>
    </a>
    <h2 class="headline">
      <span class="headline__lead">Do you have a</span>
      <span class="headline__rest">rapid response</span>
      <span class="headline__rest">plan for this?</span>
    </h2>
  </section>

  <section class="banner banner--option-two" aria-label="Banner option 2">
    <div class="photo photo--burst-pipe" role="img" aria-label="Photo of a burst red pipe spraying water"></div>
    <svg class="panel-shape" viewBox="0 0 861 222" aria-hidden="true">
      <polygon points="338,0 421,111 341,222 861,222 861,0" fill="var(--accent-red)"/>
      <polygon points="350,0 410,111 355,222 861,222 861,0" fill="var(--brand-navy)"/>
    </svg>
    <a class="brand-mark" href="#">
      <span class="brand-mark__circle"></span>
      <span class="brand-mark__name">CRESTWAY</span>
      <span class="brand-mark__tagline">RESTORATION</span>
    </a>
    <h2 class="headline">
      <span class="headline__lead">Do you have a</span>
      <span class="headline__rest">rapid response</span>
      <span class="headline__rest">plan for this?</span>
    </h2>
  </section>

</div>
</body>
</html>
```